Business card design needed

Front of Card:
I would like to have nearly 3/4 of the card from the top in a Pea Green Colour with the word 'Loftwhirl' written in a(Watermelon Red colour) in the font 'Viner Hand ITC'. Loftwhirl to be written within the Green colour of the card.

The lower 1/3 of the card I would like to have white with the words:
Home and Garden Styling smaller than the word Loftwhirl in Black in the font 'Batang', centred underneath the green section.

At the very bottom in one corner in smaller print I would like to have my contact phone number: Bea M:0419736204 and then the email address:
E: loftwhirlstyling@pemblenet.example on the other side.

Back of Card:
Back of Card to be White
On one side (Left)
I would like the Heading "Garden" in the same pea green colour as the front and in the Viner Hand ITC font. On the other half of the card I would like 'Home' in the Watermelon Red Colour (same as front colour) and in the font Viner Hand ITC.
Underneath these Headings I would like written in black and in Batang font the following list of services.

Garden Home
Garden Styling Interior Styling
Plant Selection Furniture Selection/Arrangement Garden Maintenance Setting Up Home (after move)
Hedging/Mowing Merchandise and Stylist for
Work w/Local Nurseries Marnet and Crabb

Industry/Entity Type

Business

Contact Information for Business Card

Loftwhirl
Home and Garden Styling
M: 0419736204 E: loftwhirlstyling@pemblenet.example

```html
<!DOCTYPE html>
<html lang="en">
<head>
<meta charset="utf-8">
<title>Loftwhirl – Home and Garden Styling Business Card</title>
<link rel="stylesheet" href="https://fonts.googleapis.com/css2?family=Gochi+Hand&family=Nanum+Myeongjo:wght@400;700&family=Tinos&display=swap">
<style>
  :root {
    --pea-green: #3f9b3e;
    --pea-green-deep: #338a34;
    --watermelon: #c8453d;
    --ink: #1a1a1a;
    --paper: #ffffff;
    --backdrop-top: #f4f4f4;
    --backdrop-bottom: #d9d9d9;
    --bullet-green: #4aa64a;
    --card-shadow: rgba(0, 0, 0, 0.35);
  }
  * { box-sizing: border-box; margin: 0; padding: 0; }
  html, body { width: 1200px; height: 1200px; overflow: hidden; }
  body {
    position: relative;
    background: radial-gradient(ellipse at center, var(--backdrop-top) 40%, var(--backdrop-bottom) 100%);
    font-family: "Nanum Myeongjo", serif;
    color: var(--ink);
  }
  .card {
    position: absolute;
    left: 193px;
    width: 834px;
    border-radius: 16px;
    overflow: hidden;
    background: var(--paper);
    box-shadow: 6px 8px 10px var(--card-shadow);
  }
  .card--front { top: 64px; height: 513px; }
  .card--back { top: 640px; height: 509px; }

  .leaf-field {
    position: absolute;
    left: 0; right: 0;
    background: radial-gradient(circle at 50% 40%, var(--pea-green) 0%, var(--pea-green-deep) 100%);
  }
  .card--front .leaf-field { top: 0; height: 376px; }
  .card--back .leaf-field { bottom: 0; height: 92px; }

  .brand-name {
    position: absolute;
    top: 108px; left: 0; right: 0;
    text-align: center;
    font-family: "Nanum Myeongjo", serif;
    font-weight: 700;
    font-size: 118px;
    line-height: 1;
    color: var(--watermelon);
  }
  .contact {
    position: absolute;
    top: 337px;
    display: flex;
    align-items: center;
    gap: 12px;
    font-family: "Tinos", serif;
    font-size: 21px;
    color: var(--paper);
  }
  .contact--phone { left: 10px; }
  .contact--email { right: 14px; }
  .contact svg { display: block; }

  .tagline {
    position: absolute;
    top: 376px; left: 0; right: 0; height: 137px;
    display: flex; align-items: center; justify-content: center;
    font-size: 56px;
    font-weight: 400;
    color: var(--ink);
  }

  .service-heading {
    position: absolute;
    top: 20px;
    font-family: "Gochi Hand", cursive;
    font-size: 118px;
    line-height: 1;
  }
  .service-heading--garden { left: 20px; color: var(--pea-green); }
  .service-heading--home { left: 407px; color: #a52a2a; }

  .service-list {
    position: absolute;
    list-style: none;
    font-size: 26px;
    line-height: 1.3;
    color: var(--ink);
  }
  .service-list--garden { left: 55px; top: 168px; }
  .service-list--garden li { margin-bottom: 9px; }
  .service-list--home { left: 417px; top: 142px; width: 400px; }
  .service-list--home li { margin-bottom: 6px; }
  .service-list li::before {
    content: "*";
    color: var(--bullet-green);
    margin-right: 2px;
  }
  .service-list .wrap { display: block; padding-left: 14px; }
  .service-list .wrap--flush { padding-left: 0; }
</style>
</head>
<body>

<section class="card card--front" aria-label="Business card front">
  <div class="leaf-field" role="img" aria-label="Green background with a pattern of scattered leaves"></div>
  <div class="brand-name">Loftwhirl</div>

  <div class="contact contact--phone">
    <svg width="36" height="28" viewBox="0 0 36 28" aria-hidden="true">
      <path d="M2 9 Q18 -2 34 9 L30 13 L25 10 L25 6 Q18 3 11 6 L11 10 L6 13 Z" fill="#fff"/>
      <path d="M9 12 L27 12 L33 26 L3 26 Z" fill="#fff"/>
      <circle cx="18" cy="19" r="4" fill="var(--pea-green)"/>
    </svg>
    <span>Bea M: 0419736204</span>
  </div>

  <div class="contact contact--email">
    <svg width="48" height="32" viewBox="0 0 48 32" aria-hidden="true">
      <rect x="1" y="1" width="46" height="30" fill="#fff"/>
      <path d="M1 1 L24 19 L47 1 M1 31 L18 15 M47 31 L30 15" fill="none" stroke="var(--pea-green)" stroke-width="2"/>
    </svg>
    <span>loftwhirlstyling@pemblenet.example</span>
  </div>

  <div class="tagline">Home and Garden Styling</div>
</section>

<section class="card card--back" aria-label="Business card back">
  <h2 class="service-heading service-heading--garden">Garden</h2>
  <h2 class="service-heading service-heading--home">Home</h2>

  <ul class="service-list service-list--garden">
    <li>Garden Styling</li>
    <li>Plant Selection</li>
    <li>Garden Maintenance</li>
    <li>Hedging/Mowing</li>
    <li>Work w/ Local Nurseries</li>
  </ul>

  <ul class="service-list service-list--home">
    <li>Interior Styling</li>
    <li>Furniture Selection/<span class="wrap wrap--flush">Arrangement</span></li>
    <li>Setting Up Home (after<span class="wrap">move)</span></li>
    <li>Merchandise &amp; Stylist<span class="wrap">for Marnet and Crabb</span></li>
  </ul>

  <div class="leaf-field" role="img" aria-label="Green band with a pattern of scattered leaves"></div>
</section>

</body>
</html>
```